Business Card Design Project

Business card design based on the existing logo.

Target Market(s)

Small to medium business owners and CIO's looking for professional IT services.

Industry/Entity Type

Business

Font styles to use
Serif
Sans Serif

Requirements
Must have
• Logo, company name, company details

Text to appear on the business card
Name / Title:
Leon Fairholt
CEO

Address:
Valtiro Limited
Level 3, 42 Kestle St
P O Box 462
Paraparaumu 5391

Other details:
leon@valtiro.co
Ph: 0800 519 308
Mob: +64 21 948 216
www.valtiro.co

Nice to have
• I would look at both single and double sided options. My initial thought is double sided with just the logo with the grey framing for the front and the name and details on the back. But I'm open to other design options.

```html
<!DOCTYPE html>
<html lang="en">
<head>
<meta charset="utf-8">
<title>Valtiro Business Card</title>
<link href="https://fonts.googleapis.com/css2?family=Open+Sans:wght@400;600&display=swap" rel="stylesheet">
<style>
  :root {
    --bg: #e8e6e4;
    --brand-blue: #2f6a89;
    --card-white: #ffffff;
    --ink: #3b3b3b;
    --ink-soft: #6a6a6a;
    --shadow: rgba(0, 0, 0, 0.12);
  }
  * { margin: 0; padding: 0; box-sizing: border-box; }
  html, body {
    width: 1200px;
    height: 997px;
    overflow: hidden;
    background: var(--bg);
    font-family: "Open Sans", Arial, sans-serif;
  }
  .canvas {
    position: relative;
    width: 1200px;
    height: 997px;
  }
  .card {
    position: absolute;
    width: 560px;
    height: 340px;
    box-shadow: 0 6px 18px var(--shadow);
  }
  /* Front side */
  .card-front {
    left: 90px;
    top: 110px;
    background: var(--brand-blue);
    color: var(--card-white);
  }
  .front-name {
    position: absolute;
    left: 0;
    right: 0;
    top: 128px;
    display: flex;
    align-items: center;
    justify-content: center;
    gap: 18px;
    font-size: 62px;
    font-weight: 400;
    letter-spacing: 1px;
  }
  .front-dot {
    width: 34px;
    height: 34px;
    border-radius: 50%;
    background: var(--card-white);
  }
  .front-web {
    position: absolute;
    right: 26px;
    bottom: 22px;
    font-size: 14px;
    letter-spacing: 3px;
  }
  /* Back side */
  .card-back {
    left: 550px;
    top: 530px;
    background: var(--card-white);
    color: var(--ink);
  }
  .back-web {
    position: absolute;
    right: 28px;
    top: 24px;
    font-size: 14px;
    color: var(--ink);
  }
  .holder {
    position: absolute;
    right: 28px;
    top: 86px;
    text-align: right;
  }
  .holder-name {
    font-size: 30px;
    font-weight: 400;
    color: var(--ink);
  }
  .holder-title {
    font-size: 14px;
    color: var(--ink-soft);
  }
  .back-brand {
    position: absolute;
    left: 30px;
    top: 150px;
    display: flex;
    align-items: center;
    gap: 10px;
    font-size: 34px;
    color: var(--brand-blue);
  }
  .back-dot {
    width: 20px;
    height: 20px;
    border-radius: 50%;
    background: var(--brand-blue);
  }
  .contact-list {
    position: absolute;
    left: 30px;
    bottom: 24px;
    list-style: none;
    font-size: 12.5px;
    line-height: 19px;
    color: var(--ink);
  }
  .contact-list li {
    display: flex;
    align-items: flex-start;
    gap: 8px;
  }
  .contact-icon {
    width: 13px;
    height: 13px;
    margin-top: 3px;
    flex: none;
    fill: var(--brand-blue);
  }
</style>
</head>
<body>
<main class="canvas">
  <section class="card card-front" aria-label="Card front">
    <div class="front-name"><span class="front-dot"></span>Valtiro</div>
    <div class="front-web">www.valtiro.co</div>
  </section>

  <section class="card card-back" aria-label="Card back">
    <div class="back-web">www.valtiro.co</div>
    <div class="holder">
      <div class="holder-name">Leon Fairholt</div>
      <div class="holder-title">CEO</div>
    </div>
    <div class="back-brand"><span class="back-dot"></span>Valtiro</div>
    <ul class="contact-list">
      <li>
        <svg class="contact-icon" viewBox="0 0 16 16" aria-hidden="true"><path d="M8 1 L15 8 H13 V15 H10 V10 H6 V15 H3 V8 H1 Z"/></svg>
        <span>Level 3, 42 Kestle St, P O Box 462<br>Paraparaumu 5391</span>
      </li>
      <li>
        <svg class="contact-icon" viewBox="0 0 16 16" aria-hidden="true"><path d="M1 3 H15 V13 H1 Z M1 3 L8 9 L15 3" stroke="#fff" stroke-width="1"/></svg>
        <span>leon@valtiro.co</span>
      </li>
      <li>
        <svg class="contact-icon" viewBox="0 0 16 16" aria-hidden="true"><path d="M1 5 Q8 0 15 5 L13 7 L11 5 H5 L3 7 Z M4 8 H12 L14 14 H2 Z"/></svg>
        <span>0800 519 308</span>
      </li>
      <li>
        <svg class="contact-icon" viewBox="0 0 16 16" aria-hidden="true"><path d="M4 1 H12 V15 H4 Z M5.5 3 V10 H10.5 V3 Z"/></svg>
        <span>+64 21 948 216</span>
      </li>
    </ul>
  </section>
</main>
</body>
</html>
```